Business Card for new Overseas Property Buying Business

Hi

We need a new business card for our new business.

We are Faraway Nest Finders. So we search locations on behalf of our clients to find them the ideal home.

These are mainly holiday homes in nice locations - but sometimes people are looking to relocate.

I am looking for a nice simple design - that has some class and professionalism about it. Taking inspiration from our logo.

Text wise I was thinking of maybe having something like. (THE FONT FOR THIS SHOULD BE LIKE THE WRITING IN THE ATTACHMENT WITH THE MAP ON IT)

1)
What does your dream house have (tick all that apply):
swimming pool x
private vineyard x
herb garden x
full sized football pitch x

2)
How to buy a home abroad:

Method 1:
1) Scour internet for suitable estate agents
2) Arrange hectic holiday timetable with multiple agents in multiple languages
3) Fly to destination to find property was not as it seemed
4) Feel frustrated and helpless
OR
Method 2:
Contact your expert home hunter (details overleaf) - and leave the hard work to them

The end result should give people confidence that they are dealing with a professional organisation - and feel like they can place their trust in them. I would want it to drive them to either contact us directly or visit the website.

Please include name (Gordon Tramley), position (founder), contact numbers x 2, email address, website (www.quelvatrix-moor.com)

I look forward to seeing your entries.

Reason: Hi Sorry to extend - Xmas has got in the way of my plans. I will be providing feedback. Happy Christmas to you all.

```html
<!DOCTYPE html>
<html lang="en">
<head>
<meta charset="utf-8">
<title>Dream House Card</title>
<link rel="stylesheet" href="https://fonts.googleapis.com/css2?family=Architects+Daughter&display=swap">
<style>
  :root {
    --paper: #efeeed;
    --ink: #161616;
    --tick: #6fa3a0;
    --emblem-blush: #ece2dd;
  }
  html, body {
    margin: 0;
    padding: 0;
    overflow: hidden;
  }
  .card {
    position: relative;
    width: 720px;
    height: 1200px;
    background: var(--paper);
    overflow: hidden;
    font-family: "Architects Daughter", cursive;
    color: var(--ink);
  }
  .emblem-backdrop {
    position: absolute;
    left: 330px;
    top: 120px;
    width: 860px;
    height: 1080px;
  }
  .question {
    position: absolute;
    left: 72px;
    top: 355px;
    margin: 0;
    font-size: 38px;
    font-weight: 400;
    letter-spacing: 2px;
    line-height: 52px;
    white-space: nowrap;
  }
  .wishlist {
    position: absolute;
    left: 74px;
    top: 508px;
    margin: 0;
    padding: 0;
    list-style: none;
  }
  .wishlist-item {
    position: relative;
    height: 104px;
    padding-left: 70px;
    font-size: 38px;
    letter-spacing: 2px;
    line-height: 50px;
    white-space: nowrap;
  }
  .tickbox {
    position: absolute;
    left: 0;
    top: 2px;
    width: 60px;
    height: 40px;
  }
</style>
</head>
<body>
  <main class="card">
    <svg class="emblem-backdrop" viewBox="0 0 860 1080" role="img" aria-label="Faint brand emblem backdrop">
      <circle cx="520" cy="500" r="520" fill="var(--emblem-blush)" opacity="0.7"/>
    </svg>

    <h1 class="question">What does your dream house<br>have (tick all that apply):</h1>

    <ul class="wishlist">
      <li class="wishlist-item">
        <svg class="tickbox" viewBox="0 0 60 40" aria-hidden="true">
          <rect x="10" y="24" width="11" height="10" fill="none" stroke="var(--ink)" stroke-width="2.5"/>
          <path d="M4 22 L15 31 L54 8" fill="none" stroke="var(--tick)" stroke-width="3" stroke-linecap="round" stroke-linejoin="round"/>
        </svg>
        swimming pool
      </li>
      <li class="wishlist-item">
        <svg class="tickbox" viewBox="0 0 60 40" aria-hidden="true">
          <rect x="10" y="24" width="11" height="10" fill="none" stroke="var(--ink)" stroke-width="2.5"/>
          <path d="M4 22 L15 31 L54 8" fill="none" stroke="var(--tick)" stroke-width="3" stroke-linecap="round" stroke-linejoin="round"/>
        </svg>
        private vineyard
      </li>
      <li class="wishlist-item">
        <svg class="tickbox" viewBox="0 0 60 40" aria-hidden="true">
          <rect x="10" y="24" width="11" height="10" fill="none" stroke="var(--ink)" stroke-width="2.5"/>
          <path d="M4 22 L15 31 L54 8" fill="none" stroke="var(--tick)" stroke-width="3" stroke-linecap="round" stroke-linejoin="round"/>
        </svg>
        herb garden
      </li>
      <li class="wishlist-item">
        <svg class="tickbox" viewBox="0 0 60 40" aria-hidden="true">
          <rect x="10" y="24" width="11" height="10" fill="none" stroke="var(--ink)" stroke-width="2.5"/>
          <path d="M4 22 L15 31 L54 8" fill="none" stroke="var(--tick)" stroke-width="3" stroke-linecap="round" stroke-linejoin="round"/>
        </svg>
        full sized football pitch
      </li>
    </ul>
  </main>
</body>
</html>
```